Use it Or lose it Flyer for Dental Office

Need to design a home mailer, 6x9, for a use it or lose it dental insurance campaign. Insurance benefits are not rolled over in January.  Including a new patient special for $179 for Xray, Exam, Regular Cleaning. New patients will get an tamu k tooth brush if they bring in Flyer. In back I would like to advertise for Fennoway.
Our dental office is www.wrenfolddentalga.com

```html
<!DOCTYPE html>
<html lang="en">
<head>
<meta charset="utf-8">
<title>Wrenfold Dental – Mailers</title>
<link rel="stylesheet" href="https://fonts.googleapis.com/css2?family=Playfair+Display:wght@400;700;800&family=Poppins:ital,wght@0,400;0,600;0,700;1,400;1,600&display=swap">
<style>
  :root{
    --bg:#4a4a4a;
    --green:#275a4d;
    --gold:#9a8a62;
    --gold-light:#efe6cf;
    --paper:#ffffff;
    --panel:#f1f1f2;
    --ink:#2b2b2b;
    --logo:#8f8580;
  }
  *{box-sizing:border-box;margin:0;padding:0}
  html,body{width:1181px;height:1200px;overflow:hidden;background:var(--bg)}
  body{position:relative;font-family:"Poppins",sans-serif;color:var(--ink)}
  .mailer{position:absolute;left:205px;width:795px;height:530px;background:var(--paper);overflow:hidden}
  .mailer--benefits{top:44px}
  .mailer--aligners{top:623px}
  .abs{position:absolute}
  .curves{position:absolute;inset:0;width:795px;height:530px}
  .serif-num{font-variant-numeric:lining-nums}
  .headline-panel{position:absolute;left:35px;top:0;width:362px;background:var(--green);color:#fff}
  .hours-panel{position:absolute;left:621px;top:0;width:130px;height:124px;background:var(--panel);text-align:center}
  .hours-badge{display:inline-block;margin-top:44px;background:var(--gold);color:#fff;font-family:"Playfair Display",serif;font-size:13px;padding:2px 8px;border-radius:4px;letter-spacing:.3px}
  .hours-time{font-family:"Playfair Display",serif;font-variant-numeric:lining-nums;color:var(--green);font-size:14px;margin-top:3px}
  .hours-days{font-size:8px;color:#333;margin-top:1px}
  .brand{position:absolute;left:412px;top:36px;width:170px;text-align:center;color:var(--logo)}
  .brand-mark{width:36px;height:36px;border-radius:50%;background:var(--logo);margin:0 auto 20px}
  .brand-name{font-family:"Playfair Display",serif;font-size:30px;letter-spacing:3px;line-height:1}
  .brand-sub{font-family:"Poppins",sans-serif;font-size:11px;letter-spacing:8px;margin-top:10px;padding-left:8px}
  .kicker{font-weight:600;letter-spacing:-1px}
  .display{font-family:"Playfair Display",serif;font-weight:800;line-height:.86;letter-spacing:-1px;font-variant-numeric:lining-nums}
  .contact-lead{font-size:12.5px;line-height:1.08;text-transform:uppercase;color:#333}
  .phone{display:flex;align-items:center;gap:5px;font-family:"Playfair Display",serif;font-variant-numeric:lining-nums;font-weight:700;color:var(--green);font-size:23px;white-space:nowrap}
  .phone svg{width:18px;height:18px}
  .address{font-size:12px;line-height:1.1;color:#333;border-left:1px dashed #555;padding-left:11px}
  .web{position:absolute;right:45px;color:#fff;font-size:17px;letter-spacing:.2px}
  .feature{display:flex;gap:6px;font-size:12px;line-height:1}
  .feature b{font-weight:700;display:block}
  .feature svg{width:13px;height:13px;margin-top:5px;flex:none}
</style>
</head>
<body>

<!-- Front: benefits reminder -->
<section class="mailer mailer--benefits">
  <svg class="curves" viewBox="0 0 795 530">
    <defs>
      <radialGradient id="familyTones" cx="62%" cy="50%" r="60%">
        <stop offset="0" stop-color="#ebcaa8"/>
        <stop offset=".4" stop-color="#d2ab8a"/>
        <stop offset=".75" stop-color="#5a80bb"/>
        <stop offset="1" stop-color="#e6e8eb"/>
      </radialGradient>
      <linearGradient id="fadeLeft" x1="0" x2="1">
        <stop offset="0" stop-color="#fff"/>
        <stop offset=".2" stop-color="#fff" stop-opacity="0"/>
      </linearGradient>
    </defs>
    <g role="img" aria-label="Photo of a smiling mother, son and father posed cheek to cheek">
      <path d="M399 222 C520 190 650 172 795 174 L795 530 L399 530 Z" fill="url(#familyTones)"/>
      <path d="M399 222 C520 190 650 172 795 174 L795 530 L399 530 Z" fill="url(#fadeLeft)"/>
    </g>
    <path d="M399 212 C520 172 650 155 795 153 L795 174 C650 172 520 190 399 222 Z" fill="var(--green)"/>
    <path d="M500 178 C580 150 680 128 795 124 L795 145 C680 146 590 160 500 178 Z" fill="var(--gold)"/>
    <path d="M0 115 L35 140 L35 152 L0 128 Z" fill="var(--gold)"/>
    <path d="M0 140 L35 165 L35 190 L0 165 Z" fill="var(--green)"/>
    <path d="M470 512 C495 512 495 467 525 467 L795 467 L795 530 L470 530 Z" fill="var(--green)"/>
    <rect x="0" y="512" width="795" height="18" fill="var(--green)"/>
    <g transform="translate(421 378)">
      <polygon fill="var(--green)" points="0,-46 9,-37 21,-41 24,-29 36,-27 35,-15 45,-8 38,2 44,13 33,19 32,31 20,31 13,41 3,35 -8,43 -14,33 -26,35 -28,23 -40,18 -35,7 -44,-2 -36,-11 -39,-23 -27,-26 -24,-38 -12,-35"/>
    </g>
  </svg>

  <div class="headline-panel" style="height:290px;padding:42px 0 0 12px">
    <div class="kicker" style="font-size:27px;line-height:1">DON'T LET YOUR</div>
    <div class="display" style="font-size:58px;margin-top:2px">DENTAL<br>BENEFITS</div>
    <div class="display" style="font-size:42px;margin-top:6px">EXPIRE!</div>
    <p style="font-size:14.8px;line-height:1.16;margin-top:12px;width:335px">Your insurance benefits reset on January 1st, they won't roll over. <b>Maximize them NOW</b> with our <b>Exclusive New Patient Special!</b></p>
  </div>

  <div class="abs" style="left:35px;top:290px;width:362px;height:105px;background:var(--gold);box-shadow:0 4px 6px rgba(0,0,0,.25);color:#fff">
    <div class="display abs" style="left:15px;top:15px;font-size:52px;letter-spacing:-2px">$179!</div>
    <div class="abs" style="left:153px;top:16px;height:50px;border-left:1px dashed #fff"></div>
    <div class="abs" style="left:163px;top:10px;font-weight:700;font-size:16px;line-height:1.17;letter-spacing:-.5px">Comprehensive Exam<br>Full X-Rays<br>Regular Cleaning</div>
    <div class="abs" style="left:17px;top:72px;font-style:italic;font-size:21px;color:var(--gold-light);letter-spacing:-.4px">PLUS: FREE tamu k Toothbrush</div>
  </div>

  <div class="abs" style="left:389px;top:356px;width:64px;text-align:center;color:#fff;font-style:italic;font-weight:600;font-size:9.5px;line-height:1.22">We must bring in this flyer to receive offer</div>

  <div class="abs" style="left:45px;top:430px">
    <div class="contact-lead">Call us to schedule an<br>appointment today!</div>
    <div class="phone"><svg viewBox="0 0 20 20"><rect width="20" height="20" rx="5" fill="var(--green)"/><path d="M6 4.5l2 .3.8 2.8-1.4 1a7 7 0 0 0 3.9 3.9l1-1.4 2.8.8.3 2A1.6 1.6 0 0 1 14 15.5 10 10 0 0 1 4.5 6 1.6 1.6 0 0 1 6 4.5z" fill="#fff"/></svg>(555) 014-2290</div>
  </div>
  <div class="abs address" style="left:241px;top:430px;height:58px;padding-top:12px">480 Alder Run Pkwy<br>Suite 12 Larkmoor,<br>XY 00412</div>

  <div class="brand"><div class="brand-mark"></div><div class="brand-name">WRENFOLD</div><div class="brand-sub">DENTAL</div></div>
  <div class="hours-panel"><span class="hours-badge">OFFICE HOURS</span><div class="hours-time">9:00AM - 5:00PM</div><div class="hours-days">Mondays to Fridays</div></div>
  <div class="web" style="top:473px">www.wrenfolddentalga.com</div>
</section>

<!-- Back: aligner promotion -->
<section class="mailer mailer--aligners">
  <svg class="curves" viewBox="0 0 795 530" aria-hidden="true">
    <path d="M399 212 C520 180 650 166 795 164 L795 177 C650 178 520 196 399 222 Z" fill="var(--green)"/>
    <path d="M430 198 C550 155 670 130 795 124 L795 146 C670 148 550 170 430 200 Z" fill="var(--gold)"/>
    <path d="M0 115 L35 140 L35 152 L0 128 Z" fill="var(--gold)"/>
    <path d="M0 140 L35 165 L35 190 L0 165 Z" fill="var(--green)"/>
    <path d="M460 508 C485 508 492 463 522 463 L795 463 L795 508 Z" fill="var(--green)"/>
    <rect x="0" y="508" width="795" height="22" fill="var(--green)"/>
  </svg>

  <div class="headline-panel" style="height:247px;padding:42px 0 0 8px">
    <div class="kicker" style="font-size:27px;line-height:1">TRANSFORM YOUR</div>
    <div class="display" style="font-size:52px;margin-top:3px;line-height:.9">SMILE WITH<br>FENNOWAY<sup style="font-size:14px;vertical-align:top">®</sup></div>
    <div style="display:grid;grid-template-columns:180px 170px;row-gap:8px;margin:16px 0 0 6px">
      <div class="feature"><svg viewBox="0 0 14 14"><circle cx="7" cy="7" r="6" fill="none" stroke="var(--gold)" stroke-width="1.4"/><path d="M4 7.2l2 2 4-4" fill="none" stroke="var(--gold)" stroke-width="1.4"/></svg><span><b>Nearly Invisible</b>No one will notice</span></div>
      <div class="feature"><svg viewBox="0 0 14 14"><circle cx="7" cy="7" r="6" fill="none" stroke="var(--gold)" stroke-width="1.4"/><path d="M4 7.2l2 2 4-4" fill="none" stroke="var(--gold)" stroke-width="1.4"/></svg><span><b>Comfortable</b>No metal irritation</span></div>
      <div class="feature"><svg viewBox="0 0 14 14"><circle cx="7" cy="7" r="6" fill="none" stroke="var(--gold)" stroke-width="1.4"/><path d="M4 7.2l2 2 4-4" fill="none" stroke="var(--gold)" stroke-width="1.4"/></svg><span><b>Removable</b>Eat and clean normally</span></div>
      <div class="feature"><svg viewBox="0 0 14 14"><circle cx="7" cy="7" r="6" fill="none" stroke="var(--gold)" stroke-width="1.4"/><path d="M4 7.2l2 2 4-4" fill="none" stroke="var(--gold)" stroke-width="1.4"/></svg><span><b>Fast</b>Results in 12-18 months</span></div>
    </div>
  </div>

  <div class="abs" style="left:35px;top:245px;width:362px;height:138px;background:var(--gold);padding:5px;display:flex;gap:4px">
    <div role="img" aria-label="Close-up of a smile before aligner treatment" style="flex:1;background:radial-gradient(ellipse at 50% 55%,#f3efe6 0%,#d98a80 40%,#b98870 75%,#a57a66 100%)"></div>
    <div role="img" aria-label="Close-up of a straight white smile after aligner treatment, with a clear aligner in its case" style="flex:1;background:radial-gradient(ellipse at 50% 55%,#ffffff 0%,#e08e86 40%,#c09078 75%,#a98068 100%)"></div>
  </div>

  <div class="abs" style="left:43px;top:408px">
    <div class="contact-lead" style="font-size:13.5px">Call us to get a free<br>Fennoway consultation</div>
    <div class="phone" style="font-size:26px"><svg viewBox="0 0 20 20"><rect width="20" height="20" rx="5" fill="var(--green)"/><path d="M6 4.5l2 .3.8 2.8-1.4 1a7 7 0 0 0 3.9 3.9l1-1.4 2.8.8.3 2A1.6 1.6 0 0 1 14 15.5 10 10 0 0 1 4.5 6 1.6 1.6 0 0 1 6 4.5z" fill="#fff"/></svg>(555) 014-2290</div>
  </div>
  <div class="abs address" style="left:262px;top:405px;height:60px;padding-top:12px;font-size:13.5px">480 Alder Run Pkwy<br>Suite 12 Larkmoor,<br>XY 00412</div>
  <div class="abs" style="left:43px;top:476px;font-size:16px;color:var(--green);letter-spacing:-.3px">We must Bring in this flyer to receive offer</div>

  <div class="brand"><div class="brand-mark"></div><div class="brand-name">WRENFOLD</div><div class="brand-sub">DENTAL</div></div>
  <div class="hours-panel"><span class="hours-badge">OFFICE HOURS</span><div class="hours-time">9:00AM - 5:00PM</div><div class="hours-days">Mondays to Fridays</div></div>
  <div class="web" style="top:470px">www.wrenfolddentalga.com</div>
</section>

</body>
</html>
```